Flyer-Design für Handelsunternehmen
Zielgruppe
Wir sind ein Handelsunternehmen für Produkte zur Ladungssicherung im Container.
Unsere Zielgruppe sind Speditionen, Stauer, Logistiker, Exporteure, Industrie & Handel.
Kernprodukte sind Stausäcke, Lashband, Container-Lashing, Container-Planen, Umreifungsband, Plomben sowie Halterungen von FRACHTOLUX®.
Gewünscht sind Flyer (& Broschüren) sowohl zu den einzelnen Produktgruppen wie auch als Gesamtübersicht
(Bilder und Textbeispiele auf www.PTladen17.de bzw. nach Rücksprache)
Der Flyer soll schwerpunktmäßig einen kurzen Überblick über die genannten Produktkategorien abbilden. Damit der Kunde (ausschließlich B2B) weiß, was wir anbieten.
Verkauf findet nicht nur über den Shop statt, sondern auch klassisch per Telefon, Fax und Vertriebsmitarbeiter.
Aufgabenstellung
Bilder und Textbeispiele auf www.PTladen17.de bzw. nach Rücksprache

```html
<!DOCTYPE html>
<html lang="de">
<head>
<meta charset="utf-8">
<title>Brandt &amp; Keller Ladungssicherung – Flyer</title>
<link rel="stylesheet" href="https://fonts.googleapis.com/css2?family=Raleway:wght@400;500;600;700&family=Roboto:wght@300;400;500;700&display=swap">
<style>
:root{
  --stage:#c9c9cf;
  --navy:#333d4c;
  --blue:#5865b0;
  --blue-soft:#a7b0dc;
  --gold:#d3a62a;
  --red:#b23838;
  --paper:#ffffff;
  --paper-grey:#e7e7ea;
  --text:#6b707a;
  --text-dark:#3d4350;
}
*{margin:0;padding:0;box-sizing:border-box}
html,body{width:1200px;height:2400px;overflow:hidden}
body{background:var(--stage);font-family:"Roboto",sans-serif;color:var(--text);position:relative}
.spread{position:absolute;left:24px;width:1152px;height:815px;display:flex;box-shadow:0 14px 40px rgba(0,0,0,.18)}
.spread--outside{top:330px}
.spread--inside{top:1255px}
.panel{position:relative;width:384px;height:815px;overflow:hidden}
.panel svg.deco{position:absolute;left:0;top:0;width:384px;height:815px}
.photo{position:absolute;left:0;top:0;width:384px}
.abs{position:absolute}
.h-display{font-family:"Raleway",sans-serif;text-transform:uppercase;font-weight:600;letter-spacing:.3px}
.rule{width:26px;height:2px;background:var(--blue)}
.rule--gold{background:var(--gold)}

/* outside flap */
.flap{background:var(--paper-grey);padding:40px 36px}
.flap__title{font-size:17px;line-height:1.2;color:var(--text-dark)}
.flap .rule{margin:26px 0 30px}
.flap__kicker{font-size:8.5px;font-weight:700;text-transform:uppercase;color:var(--text-dark);margin-bottom:16px}
.flap__body{font-size:9.3px;line-height:1.8;color:var(--text)}
.flap__point{font-size:9px;font-weight:700;line-height:1.7;color:var(--text-dark);margin-top:16px}
.flap__contact{position:absolute;left:36px;top:615px;font-size:10px;line-height:1.6;color:var(--blue);font-weight:500}

/* back */
.back{background:var(--navy)}
.back__content{position:absolute;left:0;top:470px;width:384px;text-align:center;color:#fff}
.back__title{font-size:15px;color:#fff;margin-bottom:26px}
.back__address{font-size:8.5px;line-height:2;color:#d7dae2;text-transform:none}

/* cover */
.cover{background:var(--navy)}
.cover__head{position:absolute;left:0;top:0;width:384px;height:130px;background:linear-gradient(#f3f4f7,#e6e9ef);padding:30px 22px 0}
.cover__kicker{font-family:"Raleway",sans-serif;font-size:8.5px;font-weight:600;color:var(--red);text-transform:uppercase;margin-bottom:10px}
.cover__headline{font-family:"Raleway",sans-serif;font-size:15.5px;font-weight:700;line-height:1.45;color:var(--blue)}
.cover__list{position:absolute;left:22px;top:485px;list-style:none;font-size:9px;line-height:2.35;color:#fff;text-transform:uppercase;letter-spacing:.2px}
.cover__brand{position:absolute;left:0;top:742px;width:286px;height:58px;background:#fff;text-align:center;padding-top:12px;font-family:"Raleway",sans-serif;font-weight:500;font-size:15px;line-height:1;color:var(--blue);text-transform:uppercase}
.cover__band{position:absolute;left:52px;top:800px;width:332px;height:15px;background:var(--blue);color:#fff;font-family:"Raleway",sans-serif;font-size:8px;text-align:right;padding:3px 14px 0 0;letter-spacing:.4px}

/* inside intro */
.intro{background:var(--paper)}
.intro__text{position:absolute;left:34px;top:300px;width:320px}
.intro__title{font-size:15px;line-height:1.25;color:var(--text-dark)}
.intro .rule{margin:14px 0 20px}
.intro__body{font-size:9px;line-height:1.85;color:var(--text)}
.ticks{list-style:none;margin-top:20px}
.ticks li{display:flex;align-items:center;gap:8px;font-family:"Raleway",sans-serif;font-size:10px;font-weight:500;letter-spacing:.6px;text-transform:uppercase;color:var(--text);line-height:1.85}
.ticks svg{width:9px;height:9px;flex:none}

/* inside contact */
.contact{background:var(--navy)}
.contact__text{position:absolute;left:0;top:610px;width:384px;text-align:center;color:#fff}
.contact__small{font-family:"Raleway",sans-serif;font-size:11px;text-transform:uppercase;letter-spacing:.5px}
.contact__big{font-size:16px;font-weight:700;line-height:1.3;margin-top:4px;color:#fff}
.contact .rule{margin:14px auto}
.contact__phone{font-family:"Raleway",sans-serif;font-size:22px;font-weight:600;color:var(--blue);letter-spacing:.5px}

/* inside services */
.services{background:var(--paper-grey)}
.services__text{position:absolute;left:36px;top:270px;width:320px}
.services__title{font-size:18px;color:var(--text-dark);margin-top:12px}
.services__sub{font-size:8.5px;text-transform:uppercase;color:var(--text);margin:12px 0 26px}
.service{display:flex;gap:16px;margin-bottom:30px}
.service__icon{width:46px;height:46px;border:2px solid var(--gold);flex:none;display:flex;align-items:center;justify-content:center}
.service__icon svg{width:26px;height:26px}
.service__name{font-family:"Raleway",sans-serif;font-size:13px;font-weight:700;text-transform:uppercase;color:var(--text-dark);margin-bottom:5px}
.service__desc{font-size:9px;line-height:1.6;color:var(--text)}
</style>
</head>
<body>

<!-- Outside spread -->
<section class="spread spread--outside">
  <article class="panel flap">
    <h2 class="flap__title h-display">Weltweit mit Sicherheit<br>transportieren</h2>
    <div class="rule"></div>
    <p class="flap__kicker">Ihre Ladungssicherung ist unser Produkt</p>
    <p class="flap__body">Wollen Sie nicht auch Ihre Kernkompetenz in den Mittelpunkt Ihrer Arbeit stellen? Und haben Sie sich nicht auch schon einmal überlegt, Dinge, die nicht zu Ihrem Kerngeschäft gehören, anderen zu überlassen? Dann kann unsere bescheidene Produktübersicht Ihnen vielleicht als Inspiration dienen, Ihre Optimierungspotenziale zu entdecken! Konzentrieren Sie Ihre Ressourcen auf Ihre Kernprodukte! Als Spezialist für Ladungssicherung konzentrieren wir uns darauf, für Sie Zeit zu sparen und Kosten zu reduzieren! Somit können Sie schneller auf die Anforderungen des Marktes reagieren!</p>
    <p class="flap__point">Ladungssicherung von Brandt &amp; Keller zum<br>Schutz von Mensch und Umwelt</p>
    <p class="flap__point">Transportsicherung im LKW – vermeidet Unfälle und<br>Wertverlust</p>
    <p class="flap__point">Ladungssicherung für Seecontainer<br>B&amp;K auf allen Weltmeeren</p>
    <p class="flap__contact">Rufen Sie an – wir beraten Sie gerne!<br>+49 2151 48830-10<br>www.PTladen17.de</p>
    <svg class="deco" viewBox="0 0 384 815" aria-hidden="true">
      <polygon points="36,740 328,660 330,674 38,754" fill="var(--blue)"/>
    </svg>
  </article>

  <article class="panel back">
    <div class="photo" role="img" aria-label="Luftaufnahme eines Güterbahnhofs mit vielen parallelen Gleisen und Waggons" style="height:420px;background:linear-gradient(160deg,#6f7561,#8a7a63 45%,#5d6068)"></div>
    <svg class="deco" viewBox="0 0 384 815" aria-hidden="true">
      <polygon points="0,400 384,300 384,815 0,815" fill="var(--navy)"/>
      <polygon points="0,388 384,288 384,300 0,400" fill="var(--blue)"/>
      <rect x="30" y="790" width="354" height="14" fill="var(--blue)"/>
    </svg>
    <div class="abs" role="img" aria-label="Dezente Weltkarte im Hintergrund" style="left:40px;top:600px;width:304px;height:150px;background:radial-gradient(ellipse at center,rgba(255,255,255,.06),rgba(255,255,255,0) 70%)"></div>
    <div class="back__content">
      <h3 class="back__title h-display">Wir beraten Sie gerne</h3>
      <p class="back__address">BRANDT &amp; KELLER<br>LADUNGSSICHERUNG<br>Lagerweg 8<br>47805 Musterstadt<br>Telefon: +49 2151 48830-10</p>
    </div>
  </article>

  <article class="panel cover">
    <div class="photo" role="img" aria-label="LKW in Fahrt auf einer Brücke, Landschaft mit Bergen im Hintergrund" style="top:110px;height:300px;background:linear-gradient(180deg,#c9ced6,#9aa39c 55%,#6c7670)"></div>
    <div class="cover__head">
      <p class="cover__kicker">Ihr Online-Shop für</p>
      <h1 class="cover__headline">Professionelles Zubehör<br>für erfolgreiche Ladungssicherung<br>Einfach. Online. Bestellen.</h1>
    </div>
    <svg class="deco" viewBox="0 0 384 815" aria-hidden="true">
      <polygon points="0,300 384,395 384,815 0,815" fill="var(--navy)"/>
      <polygon points="0,288 384,383 384,395 0,300" fill="var(--blue)"/>
    </svg>
    <ul class="cover__list">
      <li>Stausäcke</li><li>Lashband</li><li>Umreifungsband</li><li>Folie</li><li>Zurrgurte</li><li>Antiruschmatten</li><li>Plomben</li><li>Diebstahlschutz</li><li>uvm.</li>
    </ul>
    <div class="cover__brand">Brandt &amp; Keller<br><span style="font-weight:400;font-size:13px">Ladungssicherung</span></div>
    <div class="cover__band">WWW.PTLADEN17.DE</div>
  </article>
</section>

<!-- Inside spread -->
<section class="spread spread--inside">
  <article class="panel intro">
    <div class="photo" role="img" aria-label="Holzkiste mit blauem Spanngurt und Kantenschutz" style="height:290px;background:linear-gradient(135deg,#c8b596,#a88a5e 50%,#7f6a4c)"></div>
    <svg class="deco" viewBox="0 0 384 815" aria-hidden="true">
      <polygon points="0,0 110,0 0,110" fill="var(--blue-soft)"/>
      <polygon points="0,110 384,270 384,815 0,815" fill="var(--paper)"/>
      <polygon points="0,96 384,256 384,270 0,110" fill="var(--blue)"/>
      <rect x="0" y="788" width="300" height="16" fill="var(--blue)"/>
    </svg>
    <div class="intro__text">
      <h2 class="intro__title h-display">Brandt &amp; Keller<br>Ladungssicherung</h2>
      <div class="rule"></div>
      <p class="intro__body">Dank innovativer Produkte und effektiver Systemlösungen für die Ladungssicherung in Seecontainern und auf anderen Verkehrsträgern ist die Brandt &amp; Keller GmbH einer der weltweit führenden Lieferanten für Ladungssicherungs-Systeme. Was auch immer Sie sichern wollen – wir sind Ihr Experte für Ladungssicherung.</p>
      <ul class="ticks">
        <li><svg viewBox="0 0 10 10"><circle cx="5" cy="5" r="5" fill="var(--blue)"/><path d="M2.6 5.2 4.3 6.8 7.4 3.4" stroke="#fff" stroke-width="1.3" fill="none"/></svg>Fassware</li>
        <li><svg viewBox="0 0 10 10"><circle cx="5" cy="5" r="5" fill="var(--blue)"/><path d="M2.6 5.2 4.3 6.8 7.4 3.4" stroke="#fff" stroke-width="1.3" fill="none"/></svg>Sackware</li>
        <li><svg viewBox="0 0 10 10"><circle cx="5" cy="5" r="5" fill="var(--blue)"/><path d="M2.6 5.2 4.3 6.8 7.4 3.4" stroke="#fff" stroke-width="1.3" fill="none"/></svg>Kartonage</li>
        <li><svg viewBox="0 0 10 10"><circle cx="5" cy="5" r="5" fill="var(--blue)"/><path d="M2.6 5.2 4.3 6.8 7.4 3.4" stroke="#fff" stroke-width="1.3" fill="none"/></svg>Big Bags</li>
        <li><svg viewBox="0 0 10 10"><circle cx="5" cy="5" r="5" fill="var(--blue)"/><path d="M2.6 5.2 4.3 6.8 7.4 3.4" stroke="#fff" stroke-width="1.3" fill="none"/></svg>IBC Container</li>
        <li><svg viewBox="0 0 10 10"><circle cx="5" cy="5" r="5" fill="var(--blue)"/><path d="M2.6 5.2 4.3 6.8 7.4 3.4" stroke="#fff" stroke-width="1.3" fill="none"/></svg>Kanister</li>
        <li><svg viewBox="0 0 10 10"><circle cx="5" cy="5" r="5" fill="var(--blue)"/><path d="M2.6 5.2 4.3 6.8 7.4 3.4" stroke="#fff" stroke-width="1.3" fill="none"/></svg>Kisten</li>
        <li><svg viewBox="0 0 10 10"><circle cx="5" cy="5" r="5" fill="var(--blue)"/><path d="M2.6 5.2 4.3 6.8 7.4 3.4" stroke="#fff" stroke-width="1.3" fill="none"/></svg>Gitterboxen</li>
        <li><svg viewBox="0 0 10 10"><circle cx="5" cy="5" r="5" fill="var(--blue)"/><path d="M2.6 5.2 4.3 6.8 7.4 3.4" stroke="#fff" stroke-width="1.3" fill="none"/></svg>Güter auf einer Holzkonstruktion</li>
        <li><svg viewBox="0 0 10 10"><circle cx="5" cy="5" r="5" fill="var(--blue)"/><path d="M2.6 5.2 4.3 6.8 7.4 3.4" stroke="#fff" stroke-width="1.3" fill="none"/></svg>Güter im Kühlcontainer</li>
        <li><svg viewBox="0 0 10 10"><circle cx="5" cy="5" r="5" fill="var(--blue)"/><path d="M2.6 5.2 4.3 6.8 7.4 3.4" stroke="#fff" stroke-width="1.3" fill="none"/></svg>Güter auf Flatracks</li>
        <li><svg viewBox="0 0 10 10"><circle cx="5" cy="5" r="5" fill="var(--blue)"/><path d="M2.6 5.2 4.3 6.8 7.4 3.4" stroke="#fff" stroke-width="1.3" fill="none"/></svg>Güter im Seecontainer</li>
      </ul>
    </div>
  </article>

  <article class="panel contact">
    <div class="photo" role="img" aria-label="Helle Lagerhalle mit hohen Regalen voller Kartons auf Paletten" style="height:560px;background:linear-gradient(160deg,#e9ecef,#b9b3a6 45%,#7a7f8c 80%,#d9dbe0)"></div>
    <svg class="deco" viewBox="0 0 384 815" aria-hidden="true">
      <polygon points="0,560 384,540 384,815 0,815" fill="var(--navy)"/>
      <polygon points="20,548 384,528 384,540 20,560" fill="var(--blue)"/>
      <rect x="34" y="778" width="318" height="14" fill="var(--blue)"/>
    </svg>
    <div class="contact__text">
      <p class="contact__small">Wir sind für Sie da!</p>
      <p class="contact__big h-display">Fragen?<br>Wir beraten Sie gerne!</p>
      <div class="rule"></div>
      <p class="contact__phone">+49 2151 48830 - 20</p>
    </div>
  </article>

  <article class="panel services">
    <div class="photo" role="img" aria-label="Nahaufnahme eines weißen Umreifungsbands mit dunkler Metallschnalle" style="height:220px;background:linear-gradient(135deg,#d6d6d8,#b4b4b8 55%,#8e8e94)"></div>
    <svg class="deco" viewBox="0 0 384 815" aria-hidden="true">
      <polygon points="0,230 384,170 384,815 0,815" fill="var(--paper-grey)"/>
      <polygon points="60,220 384,170 384,182 60,232" fill="var(--blue)"/>
      <rect x="40" y="790" width="344" height="15" fill="var(--blue)"/>
    </svg>
    <div class="services__text">
      <div class="rule rule--gold"></div>
      <h2 class="services__title h-display">Unsere Services</h2>
      <p class="services__sub">Wie können wir Ihnen helfen?</p>
      <div class="service">
        <div class="service__icon"><svg viewBox="0 0 26 26" fill="none" stroke="var(--text-dark)" stroke-width="1.4"><rect x="6" y="3" width="14" height="20"/><path d="M9 8h8M9 12h8M9 16h5"/></svg></div>
        <div><p class="service__name">Angebot gewünscht?</p><p class="service__desc">Lorem ipsum dolor sit amet, consectetur adipiscing elit. Donec et rhoncus mi.</p></div>
      </div>
      <div class="service">
        <div class="service__icon"><svg viewBox="0 0 26 26" fill="none" stroke="var(--text-dark)" stroke-width="1.4"><path d="M3 14l9-2 6-8 2 1-3 8 6 2v2l-7-1-4 6-2-1 1-5-7-1z"/></svg></div>
        <div><p class="service__name">Lufttransport?</p><p class="service__desc">Lorem ipsum dolor sit amet, consectetur adipiscing elit. Donec et rhoncus mi.</p></div>
      </div>
      <div class="service">
        <div class="service__icon"><svg viewBox="0 0 26 26" fill="none" stroke="var(--text-dark)" stroke-width="1.4"><path d="M4 20V9h7l3 6v5"/><path d="M18 4v16h5"/><circle cx="7" cy="21" r="2"/><circle cx="14" cy="21" r="2"/></svg></div>
        <div><p class="service__name">Grosses Lager</p><p class="service__desc">Lorem ipsum dolor sit amet, consectetur adipiscing elit. Donec et rhoncus mi.</p></div>
      </div>
      <div class="service">
        <div class="service__icon"><svg viewBox="0 0 26 26" fill="none" stroke="var(--text-dark)" stroke-width="1.4"><circle cx="13" cy="13" r="4"/><path d="M13 3v4M13 19v4M3 13h4M19 13h4M6 6l3 3M17 17l3 3M6 20l3-3M17 9l3-3"/></svg></div>
        <div><p class="service__name">Service Hotline</p><p class="service__desc">Lorem ipsum dolor sit amet, consectetur adipiscing elit. Donec et rhoncus mi.</p></div>
      </div>
    </div>
  </article>
</section>

</body>
</html>
```